Lorna Tess Tresses Fancy Business Card’s

I want my business cards to be elite, original and very classy. I want the business cards to match the colors of my logo and to match the design posted. I would love the design of the picture I posted

I want the card all white .
The dripping on the top of the card I want it to match the pink color in my logo that’s also posted .
I need my logo on the business card !
I need my Instagram- @lorna.tess.tresses__
And my phone number - 582 907 3365

Target Market(s)

My target market is young woman age 23 to older woman to the age of 65
I want both older and younger women to love my design . I don’t want any cheap looking business cards

Industry/Entity Type

Hair And Beauty

Contact Information for Business Card

Add my logo
Add my Instagram- @lorna.tess.tresses__
My number - 582 907 3365
My website- www.lornatesstresses.example

Font styles to use
Serif
Script

Colors
ffffff
e667a6
e34298

Requirements
Must have
• The business cards must have my logo, my number , my website, and my Instagram!
Nice to have
• Nice to have glitter words that match my logo
• The business cards must look classy and mature
• I want them to be very unique!!
Should not have
• Should not have any colors that doesn’t match my logo ! This is very important! Please

```html
<!DOCTYPE html>
<html lang="en">
<head>
<meta charset="utf-8">
<title>Lorna Tess Tresses – Business Cards</title>
<link rel="stylesheet" href="https://fonts.googleapis.com/css2?family=Lato:wght@400&family=Playfair+Display:wght@600&display=swap">
<style>
  :root {
    --stage: #2e2e2e;
    --pink: #e34298;
    --pink-soft: #e667a6;
    --black-card: #1c1c1c;
    --white: #ffffff;
    --silver: #c8c8c8;
    --silver-dark: #8a8a8a;
    --silver-light: #eeeeee;
  }
  * { box-sizing: border-box; margin: 0; padding: 0; }
  html, body {
    width: 1200px;
    height: 866px;
    overflow: hidden;
    background: var(--stage);
    font-family: "Lato", sans-serif;
  }
  .stage {
    width: 1200px;
    height: 866px;
    display: flex;
    align-items: center;
    justify-content: center;
    gap: 40px;
  }
  .card {
    position: relative;
    width: 540px;
    height: 309px;
    overflow: hidden;
    box-shadow: 0 6px 18px rgba(0,0,0,0.45);
  }
  .card--front { background: var(--pink); color: var(--white); }
  .card--back  { background: var(--black-card); }

  .glitter-band {
    position: absolute;
    left: 0; right: 0; bottom: 0;
    height: 40px;
    background: linear-gradient(90deg, var(--silver-dark), var(--silver-light) 25%, var(--silver) 50%, var(--silver-light) 75%, var(--silver-dark));
  }

  .brand-name {
    position: absolute;
    left: 0; right: 0;
    text-align: center;
    font-family: "Playfair Display", serif;
    font-weight: 600;
    letter-spacing: 0.5px;
    white-space: nowrap;
  }
  .card--front .brand-name { top: 52px; font-size: 36px; color: var(--white); }
  .card--back  .brand-name { top: 104px; font-size: 38px; color: var(--silver); }

  .contact {
    position: absolute;
    left: 0; right: 0;
    top: 132px;
    display: flex;
    flex-direction: column;
    align-items: center;
    font-size: 17px;
    line-height: 26px;
    font-weight: 400;
    color: var(--white);
  }
  .contact-line { display: flex; align-items: center; gap: 7px; white-space: nowrap; }
  .contact-dot {
    width: 13px; height: 13px;
    border: 1.6px solid var(--white);
    border-radius: 50%;
  }
</style>
</head>
<body>
  <main class="stage">
    <section class="card card--front" aria-label="Business card front">
      <p class="brand-name">Lorna Tess Tresses</p>
      <div class="contact">
        <p class="contact-line contact-line--phone">582 907 3365</p>
        <p class="contact-line contact-line--web">www.lornatesstresses.example</p>
        <p class="contact-line contact-line--social"><span class="contact-dot"></span>@lorna.tess.tresses__</p>
      </div>
      <div class="glitter-band" role="img" aria-label="Silver glitter band"></div>
    </section>

    <section class="card card--back" aria-label="Business card back">
      <p class="brand-name">Lorna Tess Tresses</p>
      <div class="glitter-band" role="img" aria-label="Silver glitter band"></div>
    </section>
  </main>
</body>
</html>
```